Cigarette Packaging for a luxury smoking brand

I need to do a new packaging for my cigarette brand new flavor and i need you to provide me with the source files and also with renders with 3d mockups. The design must include the cigarette box for 20 cigs, the outer box that contains 10 package of 20 cigs each, and the cigarrette must also be designed using black paper. I will provide our logo and other information that's required. The new flavor is called "Orvo". You can see our other product designs at www.torvel.uk but the layout you can freely change it as long the design contains the name "TORVEL" and the logo symbol, and the flavor name "Orvo"
Updates

Dear Designers. Thank you very much for your work.
Sadly i was unaware that the www.torvel.uk website was attacked by a malware and that the page was offline. I apologize for that. The issue is solved now and the page is back on. I like some of the designs seen, but sadly the designs are too focused on the logo and not on the stylish or luxury concept. I suggest you have a look on how we use the logo on the existing designs on torvel.uk and find a way to make a unique design based on your creativity. Please feel free to message me if you have any question or suggestion and i will be happy to assist. Focus more on the name and flavor and a smaller logo somewhere in the package and not big logo.

Target Market(s)

Tobacco consumers

Industry/Entity Type

tobacco

Colors

Designer to choose only greyscale colors for use in the design.

Requirements
Must have
• My name and logo, name can be any color but logo is usually on debossed or embossed with gold foil
Nice to have
• i would prefer a dark or black packaging
Should not have
• pink nor girly colors,

```html
<!DOCTYPE html>
<html lang="en">
<head>
<meta charset="utf-8">
<title>TORVEL Orvo – Pack Front</title>
<link href="https://fonts.googleapis.com/css2?family=Marcellus&family=Cinzel:wght@500;600&family=Great+Vibes&display=swap" rel="stylesheet">
<style>
  :root{
    --bg:#dcdcdc;
    --pack:#242424;
    --pack-lid:#1f1f1f;
    --seam:#161616;
    --gold:#d1b06a;
    --gold-light:#ecd9a6;
    --gold-deep:#a88848;
    --ink-soft:#cfcfcf;
  }
  *{margin:0;padding:0;box-sizing:border-box}
  html,body{width:1200px;height:1200px;overflow:hidden;background:var(--bg)}
  .canvas{position:relative;width:1200px;height:1200px}
  .pack-front{
    position:absolute;left:310px;top:130px;width:580px;height:940px;
    background:var(--pack);border-radius:14px;overflow:hidden;
  }
  .lid{position:absolute;left:0;top:0;width:100%;height:310px;background:var(--pack-lid);border-bottom:3px solid var(--seam)}
  .rope-band{position:absolute;left:0;width:100%;height:9px;
    background:linear-gradient(90deg,var(--gold-deep),var(--gold-light),var(--gold),var(--gold-light),var(--gold-deep))}
  .rope-band.top{top:60px}
  .rope-band.bottom{bottom:34px}
  .brand-mark{position:absolute;top:200px;left:0;width:100%;display:flex;justify-content:center;align-items:center;gap:12px}
  .brand-mark .dot{width:14px;height:14px;border:2px solid var(--gold);transform:rotate(45deg)}
  .brand-mark span{font-family:'Marcellus',serif;color:var(--gold);font-size:26px;letter-spacing:6px}
  .brand-name{position:absolute;top:335px;width:100%;text-align:center;font-family:'Marcellus',serif;
    font-size:84px;letter-spacing:4px;color:var(--gold)}
  .descriptor{position:absolute;top:438px;width:100%;text-align:center;font-family:'Cinzel',serif;
    font-weight:600;font-size:16px;letter-spacing:1.5px;color:var(--ink-soft)}
  .pinstripe-field{position:absolute;left:18px;right:18px;top:520px;bottom:46px;
    background:linear-gradient(180deg,rgba(200,200,200,0) 0%,rgba(200,200,200,.08) 40%,rgba(200,200,200,.16) 100%)}
  .flavor-frame{position:absolute;left:150px;top:560px;width:270px;height:346px}
  .flavor-name{position:absolute;top:554px;width:100%;text-align:center;font-family:'Great Vibes',cursive;
    font-size:34px;color:var(--gold)}
  .pack-count{position:absolute;top:830px;width:100%;text-align:center;font-family:'Cinzel',serif;
    font-weight:500;font-size:15px;line-height:20px;letter-spacing:.8px;color:var(--ink-soft)}
</style>
</head>
<body>
<div class="canvas">
  <div class="pack-front">
    <div class="lid"></div>
    <div class="rope-band top" role="img" aria-label="Gold twisted rope border"></div>

    <div class="brand-mark"><i class="dot"></i><span>TORVEL</span></div>

    <div class="brand-name">TORVEL</div>
    <div class="descriptor">FILTER CIGARETTES</div>

    <div class="pinstripe-field" role="img" aria-label="Fine vertical grey and gold pinstripe pattern"></div>

    <svg class="flavor-frame" viewBox="0 0 270 346" aria-hidden="true">
      <path d="M90 16 H10 Q2 16 2 24 V346 M180 16 H260 Q268 16 268 24 V346" fill="none" stroke="var(--gold)" stroke-width="2"/>
    </svg>
    <div class="flavor-name">Orvo</div>

    <div class="pack-count">KING SIZE<br>20 CLASS A CIGARETTES</div>

    <div class="rope-band bottom" role="img" aria-label="Gold twisted rope border"></div>
  </div>
</div>
</body>
</html>
```